Tarbery's - Irish Shortbread

Tarbery’s Irish Shortbread
We are looking for a Stand-Up Pouch design – (no window no zip) that will have different flavoured all-butter shortbread in the collection. We love vintage and kitsch as a company but do not have to head in that direction. We are font lovers and would happily have a Font Driven Design for packaging. For this project we were thinking about water colours to define the flavours or Graffiti Package Design. We have 6 flavours, they are:
Irish Shortbread - Ginger Shortbread - Espresso Shortbread - Parmesan and Poppy Seed Shortbread - Strawberry Shortbread - Butterscotch Shortbread.
The size of the pouch is 12cm x 17 cm. There needs to be a hanging hole at the top. We have uploaded a couple of images. What we like is the intensity of colour, clarity of flavour and words. This needs to feel familiar yet fresh on the shelf and not merge with other packaging at the supermarket.
We are also fans of 80s Graffiti designs for packaging – see a few attached images.
I have also attached the brand

```html
<!DOCTYPE html>
<html lang="en">
<head>
<meta charset="utf-8">
<title>Tarbery's Irish Shortbread – Box Panels</title>
<link rel="stylesheet" href="https://fonts.googleapis.com/css2?family=Permanent+Marker&family=Oswald:wght@400;500&family=Cormorant+Garamond:wght@500&family=Arimo:wght@400;700&display=swap">
<style>
  :root{
    --stage:#e1ab1d;
    --lemon:#ecec3a;
    --lemon-soft:#f3f08c;
    --orange-wash:#f0a33a;
    --green-wash:#8fce3e;
    --paper:#f4f4f2;
    --ink:#2a2327;
    --plum:#8c2a86;
    --berry:#d9234b;
    --gold:#e9ae26;
    --canada-red:#d8262e;
  }
  *{box-sizing:border-box;margin:0;padding:0}
  html,body{width:1200px;height:614px;overflow:hidden}
  body{background:var(--stage);position:relative;font-family:"Oswald",sans-serif;color:var(--ink)}

  .brand-mark{position:absolute;top:54px;right:70px;font-family:"Oswald",sans-serif;font-weight:500;font-size:44px;color:var(--ink);letter-spacing:1px}

  .panel{position:absolute;top:120px;height:420px;overflow:hidden;box-shadow:0 14px 30px rgba(90,55,0,.25)}
  .panel-front{left:210px;width:300px}
  .panel-back{left:560px;width:385px}

  .wash{position:absolute;inset:0}
  .panel-front .wash{background:
      radial-gradient(circle at 8% 6%, var(--green-wash) 0, transparent 16%),
      radial-gradient(circle at 10% 96%, var(--orange-wash) 0, transparent 32%),
      linear-gradient(180deg, var(--lemon) 0, var(--lemon-soft) 48%, var(--paper) 56%, var(--paper) 100%)}
  .panel-back .wash{background:
      radial-gradient(circle at 92% 8%, var(--orange-wash) 0, transparent 30%),
      radial-gradient(circle at 85% 70%, var(--orange-wash) 0, transparent 26%),
      linear-gradient(180deg, var(--paper) 0, var(--lemon-soft) 28%, var(--lemon) 60%, var(--lemon) 100%)}

  .hang-hole{position:absolute;top:22px;left:50%;width:12px;height:12px;margin-left:-6px;border-radius:50%;background:var(--ink)}

  .name{position:absolute;left:0;right:0;text-align:center;font-family:"Oswald",sans-serif;font-weight:500;color:var(--ink)}
  .panel-front .name{top:52px;font-size:38px}
  .tagline{position:absolute;left:0;right:0;text-align:center;font-size:7px;letter-spacing:3px;text-transform:uppercase}
  .panel-front .tagline{top:104px}

  .size-tag{position:absolute;top:128px;left:72px;width:156px;height:20px;background:var(--ink);color:#fff;font-size:12px;text-align:center;line-height:20px;letter-spacing:.5px}
  .title{position:absolute;left:0;right:0;text-align:center;font-family:"Permanent Marker",cursive;line-height:.95}
  .title-1{top:150px;font-size:34px;color:var(--ink)}
  .title-2{top:184px;font-size:46px;color:var(--plum)}
  .title-3{top:228px;font-size:32px;color:var(--ink)}

  .splash{position:absolute;left:18px;top:280px;width:130px;height:110px;border-radius:46% 54% 40% 60%/50% 44% 56% 50%;background:linear-gradient(135deg,var(--plum),var(--berry) 60%,#e8413f)}
  .claims{position:absolute;left:34px;top:306px;color:#fff;font-size:10px;line-height:14px;letter-spacing:.3px}
  .net-wt{position:absolute;left:36px;bottom:0;width:42px;height:40px;background:var(--ink);color:#fff;text-align:center;font-family:"Cormorant Garamond",serif;font-size:8px;padding-top:5px}
  .net-wt b{display:block;font-size:13px;font-weight:500}

  .fr-ring{position:absolute;right:14px;top:262px;width:130px;height:130px}
  .fr-text{position:absolute;right:20px;top:290px;width:118px;text-align:center;font-family:"Cormorant Garamond",serif;color:var(--ink)}
  .fr-text small{display:block;font-family:"Oswald",sans-serif;font-size:7px;line-height:8px}
  .fr-text .l1{display:block;font-size:22px;line-height:22px}
  .fr-text .l2{display:block;font-size:26px;line-height:26px}
  .fr-text .l3{display:block;font-size:17px;line-height:18px}
  .origin-badge{position:absolute;right:104px;top:254px;width:36px;height:36px;border-radius:50%;background:var(--paper);border:2px solid var(--canada-red)}

  .ingredients{position:absolute;left:16px;top:196px;width:175px;font-family:"Arimo",sans-serif;font-size:6.4px;line-height:8.2px;color:#3a3438}
  .ingredients p+p{margin-top:3px}
  .maker{position:absolute;left:16px;top:318px;width:175px;display:flex;justify-content:space-between;align-items:flex-end}
  .maker address{font-style:normal;font-family:"Arimo",sans-serif;font-size:7px;line-height:9px;letter-spacing:.8px}
  .maker .name{position:static;font-size:22px;text-align:right}

  .nutrition{position:absolute;left:200px;top:196px;width:168px;background:#fff;border:1px solid var(--ink);padding:4px 5px;font-family:"Arimo",sans-serif;font-size:6px;line-height:7.6px}
  .nutrition h2{font-size:9px;line-height:10px;font-weight:700}
  .nutrition .serving{border-bottom:3px solid var(--ink);padding-bottom:2px}
  .nutrition table{width:100%;border-collapse:collapse}
  .nutrition td{border-bottom:.5px solid var(--ink);padding:.5px 0}
  .nutrition td:last-child{text-align:right}
  .nutrition .in{padding-left:6px}
  .nutrition .thick td{border-bottom:2px solid var(--ink)}
  .nutrition .foot{font-size:5px;line-height:6px;margin-top:2px}
</style>
</head>
<body>

<div class="brand-mark">Tarbery’s</div>

<section class="panel panel-front" aria-label="Front panel">
  <div class="wash" role="img" aria-label="Yellow watercolour wash with orange and green bleeds fading to white"></div>
  <span class="hang-hole"></span>
  <div class="name">Tarbery’s</div>
  <div class="tagline">Irish Shortbread</div>
  <div class="size-tag">12 COOKIES BITE SIZE</div>
  <div class="title title-1">TRADITIONAL</div>
  <div class="title title-2">IRISH</div>
  <div class="title title-3">SHORTBREAD</div>

  <div class="splash" role="img" aria-label="Purple and red paint splash"></div>
  <div class="claims">NO ADDITIVES<br>NO ADDED PRESERVATIVES<br>NO ADDED COLOURS<br>ALL BUTTER</div>
  <div class="net-wt">Net Wt.<b>144g</b></div>

  <svg class="fr-ring" viewBox="0 0 130 130" aria-hidden="true"><circle cx="65" cy="65" r="58" fill="none" stroke="var(--gold)" stroke-width="7"/></svg>
  <span class="origin-badge"></span>
  <div class="fr-text">
    <small>12 BISCUIT TAILLE<br>DE MORSURE</small>
    <span class="l1">Sablé</span>
    <span class="l2">Irlandais</span>
    <span class="l3">Traditionnel</span>
  </div>
</section>

<section class="panel panel-back" aria-label="Back panel">
  <div class="wash" role="img" aria-label="White fading into yellow watercolour wash with orange bleeds"></div>

  <div class="ingredients">
    <p>Ingredient List: Enriched flour, Butter, Icing Sugar, Vanilla Extract (Artificial), skim milk, carrageenan, mono- and diglycerides, cellulose gum, polysorbate 80), Espresso Instant Coffee, Turmeric.</p>
    <p>Liste d’ingrédients : Farine enrichie, beurre, amidon de maïs modifié, sucre glace, extrait de vanille (arôme à fouetter, lait écrémé, carraghénine, mono- et diglycérides, gomme de cellulose, polysorbate 80), café expresso instantané, curcuma.</p>
  </div>

  <div class="maker">
    <address>Manufactured by<br>Harbour Lane Foods Inc<br>Kinvara, PE, C0B2K0<br>Canada</address>
    <div class="name">Tarbery’s</div>
  </div>

  <div class="nutrition">
    <h2>Nutrition Facts<br>Valeur nutritive</h2>
    <div class="serving">Per 2 cookies (24 g)<br>pour 2 biscuit (24 g)</div>
    <table>
      <tr class="thick"><td><b>Calories 120</b></td><td>% Daily Value*</td></tr>
      <tr><td><b>Fat / Lipides</b> 7 g</td><td>9 %</td></tr>
      <tr><td class="in">Saturated / saturés 4.5 g</td><td>24 %</td></tr>
      <tr><td class="in">+ Trans / trans 0.4 g</td><td></td></tr>
      <tr><td><b>Carbohydrate / Glucides</b> 12 g</td><td>1 %</td></tr>
      <tr><td class="in">Fibre / Fibres 0 g</td><td>1 %</td></tr>
      <tr><td class="in">Sugars / Sucres 1 g</td><td>1 %</td></tr>
      <tr><td><b>Protein / Protéines</b> 2 g</td><td></td></tr>
      <tr><td><b>Cholesterol / Cholestérol</b> 20 mg</td><td></td></tr>
      <tr class="thick"><td><b>Sodium</b> 55 mg</td><td>2 %</td></tr>
      <tr><td>Potassium 10 mg</td><td>0 %</td></tr>
      <tr><td>Calcium 0 mg</td><td>0 %</td></tr>
      <tr><td>Iron / Fer 0.5 mg</td><td>3 %</td></tr>
    </table>
    <div class="foot">*5% or less is a little, 15% or more is a lot<br>*5% ou moins c’est peu, 15% ou plus c’est beaucoup</div>
  </div>
</section>

</body>
</html>
```